Dental marketing ad poster

I recently opened a new dental practice about 2 months ago and would like to have an ad designed for an A-frame poster to place outside our office. The goal of this ad is to attract and appeal to potential patients so they feel encouraged to come into the practice.
I’m leaving the creative direction up to you—I’d like to see what you can come up with. The ad can be funny or serious, but it should be eye-catching and patient-focused. Please highlight that we provide crowns, implants and teeth whitening.
My theme color is green but I’ll accept any color
Let me see your ideas!
Dentistry

```html
<!DOCTYPE html>
<html lang="en">
<head>
<meta charset="utf-8">
<title>Maplecrest Dentistry – A-Frame Poster</title>
<link rel="stylesheet" href="https://fonts.googleapis.com/css2?family=Lobster&family=Montserrat:wght@500;600;700;800&display=swap">
<style>
  :root {
    --page-bg: #e9eeed;
    --poster-top: #ffffff;
    --poster-mid: #e3f3f8;
    --poster-low: #bfe6f4;
    --teal-deep: #0f6f5e;
    --teal-main: #1a8a72;
    --teal-light: #7fd2c2;
    --brand-green: #1f8a3f;
    --ink-dark: #2b2b2b;
    --white: #ffffff;
  }
  * { margin: 0; padding: 0; box-sizing: border-box; }
  html, body {
    width: 1200px; height: 715px; overflow: hidden;
    background: var(--page-bg);
    font-family: "Montserrat", Arial, sans-serif;
  }
  .poster {
    position: absolute; left: 347px; top: 0;
    width: 505px; height: 715px; overflow: hidden;
    background: linear-gradient(180deg, var(--poster-top) 0%, var(--poster-top) 30%, var(--poster-mid) 60%, var(--poster-low) 100%);
  }
  .portrait {
    position: absolute; left: 118px; top: 63px;
    width: 270px; height: 270px; border-radius: 50%;
    background: radial-gradient(circle at 50% 40%, #1f8f7a 0%, var(--teal-deep) 100%);
    box-shadow: 0 0 0 6px var(--white);
  }
  .headline { position: absolute; left: 0; top: 315px; width: 505px; height: 140px; }
  .headline .script { font-family: "Lobster", cursive; fill: var(--teal-deep); }
  .headline .smile { font-family: "Montserrat", sans-serif; font-weight: 800; fill: url(#smileFill); stroke: var(--teal-main); stroke-width: 1.4; }
  .passion {
    position: absolute; left: 0; top: 450px; width: 505px; text-align: center;
    font-weight: 600; font-size: 27px; letter-spacing: 9px; color: var(--ink-dark);
    padding-left: 9px;
  }
  .brand-name {
    position: absolute; left: 0; top: 484px; width: 505px; text-align: center;
    font-weight: 700; color: var(--brand-green); line-height: 1;
  }
  .brand-name .word { display: block; font-size: 42px; }
  .brand-name .sub { display: block; font-size: 19px; letter-spacing: 6px; margin-top: 4px; padding-left: 6px; }
  .provide-band {
    position: absolute; left: 148px; top: 570px; width: 212px; height: 18px;
    background: linear-gradient(90deg, rgba(26,138,114,0) 0%, var(--teal-light) 25%, var(--teal-light) 75%, rgba(26,138,114,0) 100%);
    color: var(--white); font-weight: 600; font-size: 12.5px; text-align: center; line-height: 18px;
  }
  .service {
    position: absolute; height: 28px; width: 166px; border-radius: 14px;
    background: linear-gradient(180deg, #2a9a82 0%, var(--teal-deep) 100%);
    border: 1.5px solid var(--teal-light);
    color: var(--white); font-weight: 700; font-size: 15px; line-height: 25px;
    padding-left: 32px; text-align: center;
  }
  .service .icon {
    position: absolute; left: 2px; top: 1px; width: 23px; height: 23px; border-radius: 50%;
    background: var(--white);
  }
  .service .icon svg { position: absolute; left: 5px; top: 4px; }
  .service.crowns { left: 79px; top: 591px; }
  .service.implants { left: 260px; top: 591px; }
  .service.whitening { left: 169px; top: 623px; padding-left: 26px; }
  .contact-band {
    position: absolute; left: 0; top: 672px; width: 505px; height: 32px;
    background: var(--teal-deep); color: var(--white);
    display: flex; align-items: center; justify-content: space-between; padding: 0 14px 0 22px;
    font-weight: 600; font-size: 15px;
  }
  .contact-item { display: flex; align-items: center; gap: 7px; }
</style>
</head>
<body>
  <main class="poster">
    <div class="portrait" role="img" aria-label="Smiling dentist in navy scrubs with arms crossed, photographed against a teal circle"></div>

    <svg class="headline" viewBox="0 0 505 140" aria-label="Your smile is our">
      <defs>
        <linearGradient id="smileFill" x1="0" y1="0" x2="0" y2="1">
          <stop offset="0" stop-color="#e9f8f4"/>
          <stop offset="1" stop-color="#5cbfae"/>
        </linearGradient>
      </defs>
      <text class="smile" x="97" y="107" font-size="94" textLength="308" lengthAdjust="spacingAndGlyphs">SMILE</text>
      <text class="script" x="101" y="42" font-size="38">Your</text>
      <text class="script" x="316" y="119" font-size="30">is our</text>
    </svg>

    <div class="passion">PASSION AT</div>

    <div class="brand-name">
      <span class="word">Maplecrest</span>
      <span class="sub">DENTISTRY</span>
    </div>

    <div class="provide-band">WE PROVIDE</div>

    <div class="service crowns">
      <span class="icon"><svg width="13" height="15" viewBox="0 0 13 15"><path d="M2 2c2-2 3 0 4.5 0S9 0 11 2c1.5 2 0 5-1 7l-1 5-1.5-4h-2L4 14 3 9C2 7 .5 4 2 2z" fill="none" stroke="#0f6f5e" stroke-width="1.3"/></svg></span>
      Crowns
    </div>
    <div class="service implants">
      <span class="icon"><svg width="13" height="15" viewBox="0 0 13 15"><path d="M2 2c2-2 3 0 4.5 0S9 0 11 2c1 1.5 .5 3 0 4H2C1.5 5 1 3.5 2 2zM4 8h5M4.5 10h4M5 12h3" fill="none" stroke="#0f6f5e" stroke-width="1.3"/></svg></span>
      Implants
    </div>
    <div class="service whitening">
      <span class="icon"><svg width="13" height="15" viewBox="0 0 13 15"><path d="M2 2c2-2 3 0 4.5 0S9 0 11 2c1.5 2 0 5-1 7l-1 5-1.5-4h-2L4 14 3 9C2 7 .5 4 2 2z" fill="none" stroke="#0f6f5e" stroke-width="1.3"/></svg></span>
      Teeth Whitening
    </div>

    <footer class="contact-band">
      <span class="contact-item">
        <svg width="17" height="17" viewBox="0 0 17 17"><circle cx="8.5" cy="8.5" r="8.5" fill="#fff"/><path d="M5.3 4.2l1.6-.3 1 2.3-1 .8c.5 1.2 1.3 2 2.5 2.6l.8-1 2.3 1-.3 1.6c-3.6.4-7.3-3.4-6.9-7z" fill="#0f6f5e"/></svg>
        (555) 014-2290
      </span>
      <span class="contact-item">
        <svg width="17" height="17" viewBox="0 0 17 17" fill="none" stroke="#fff" stroke-width="1.3"><circle cx="8.5" cy="8.5" r="7.5"/><ellipse cx="8.5" cy="8.5" rx="3.2" ry="7.5"/><path d="M1 8.5h15M2.5 4.5h12M2.5 12.5h12"/></svg>
        www.maplecrestdentalco.com
      </span>
    </footer>
  </main>
</body>
</html>
```